Aid, Development & Consulting Firm

Harwell Bracegirdle Consulting Pty Ltd is a small firm in Australia whose principal works in the area of aid and development. His experience is broad ranging from aid project design and evaluation; to offering security advice in running aid operations in dangerous situations. He works with governments and private firms in conducting training for personnel travelling to work in dangerous or difficult regions. He has worked for many years with NGO's (aid organisations) and consults to the WCF. He works in locations all over the globe which include trouble spots like Iraq and Sudan, to sleepier locales like Samoa and Fiji. Being on Asia's doorstep much time is spent in Asia eg Indonesia, Vietnam. He is often called on to monitor and evaluate aid projects throughtout the globe.

Target Market(s)

Government Aid Divisions eg in Oz, FendCor; WCF; NGO's and consulting firms who work in developing countries

Industry/Entity Type

Security

Requirements
Nice to have
• Try and incorporate a global feel without being obvious i.e. no starving children as the primary work done is a step beyond obvious aid relief. Something very simple but bold and stylish as card holder is not a "touchy" feely person
Should not have
• No starving kid type scenarios. Prefer no pictures

```html
<!DOCTYPE html>
<html lang="en">
<head>
<meta charset="utf-8">
<title>Harwell Bracegirdle Consulting – Business Card</title>
<link href="https://fonts.googleapis.com/css2?family=Roboto+Condensed:wght@500&family=Open+Sans:wght@400;600&family=Arimo:ital,wght@0,400;0,700;1,400&display=swap" rel="stylesheet">
<style>
  :root {
    --forest: #2e5e0b;
    --leaf: #62ad15;
    --lime: #a2ef26;
    --accent: #6cc61c;
    --ink: #1f1f1f;
    --paper: #ffffff;
    --backdrop: #ffffff;
  }
  * { margin: 0; padding: 0; box-sizing: border-box; }
  html, body { width: 1200px; height: 427px; overflow: hidden; background: var(--backdrop); }
  .stage { position: relative; width: 1200px; height: 427px; }

  .card {
    position: absolute; top: 83px; width: 452px; height: 250px;
    background: var(--paper); overflow: hidden;
    box-shadow: 14px 10px 12px rgba(0,0,0,0.45);
  }
  .card--front { left: 92px; }
  .card--back { left: 643px; width: 453px; }

  .band { position: absolute; top: 0; bottom: 0; }
  .card--front .band {
    left: 372px; right: 0;
    background: linear-gradient(90deg, var(--lime) 0%, var(--leaf) 55%, var(--forest) 100%);
  }
  .card--back .band--panel { left: 0; width: 232px; background: var(--forest); }
  .card--back .band--strip {
    left: 232px; width: 62px;
    background: linear-gradient(90deg, var(--leaf) 0%, var(--lime) 100%);
  }

  .brand {
    position: absolute; display: flex; align-items: center; gap: 8px;
    font-family: "Roboto Condensed", sans-serif; font-weight: 500;
    color: var(--forest); line-height: 1.1;
  }
  .brand__mark { background: var(--leaf); flex: none; }
  .card--front .brand { left: 23px; top: 22px; font-size: 17px; }
  .card--front .brand__mark { width: 34px; height: 34px; }
  .card--back .brand { left: 315px; top: 204px; font-size: 12px; }
  .card--back .brand__mark { width: 22px; height: 22px; }

  .person { position: absolute; left: 22px; top: 84px; font-family: "Arimo", sans-serif; }
  .person__name { font-size: 15.5px; font-weight: 700; color: var(--forest); letter-spacing: 0.3px; }
  .person__role { font-size: 12px; font-style: italic; color: var(--ink); margin-top: 3px; }

  .contact { position: absolute; left: 22px; top: 126px; font-family: "Arimo", sans-serif; font-size: 11px; color: var(--ink); line-height: 13px; list-style: none; }
  .contact__label { color: var(--accent); }

  .address {
    position: absolute; font-family: "Open Sans", sans-serif; font-weight: 600;
    font-size: 10px; color: var(--accent); letter-spacing: 0.5px; white-space: nowrap;
  }
  .card--front .address { left: 22px; top: 217px; }
  .card--back .address {
    left: 27px; top: 12px; transform-origin: 0 0; transform: rotate(90deg);
    font-weight: 400; font-size: 8.5px; letter-spacing: 1px;
  }
</style>
</head>
<body>
<main class="stage">
  <section class="card card--front" aria-label="Business card front">
    <div class="band" role="img" aria-label="Decorative green colour band"></div>
    <div class="brand">
      <span class="brand__mark"></span>
      <span>Harwell Bracegirdle<br>Consulting Pty Ltd</span>
    </div>
    <div class="person">
      <p class="person__name">B. Harwell Bracegirdle</p>
      <p class="person__role">Director</p>
    </div>
    <ul class="contact">
      <li><span class="contact__label">m |</span> +61 (0) 400 555 123</li>
      <li><span class="contact__label">t |</span> +61 8 8000 5471</li>
      <li><span class="contact__label">e |</span> harwell@bracemail.com</li>
    </ul>
    <p class="address">27 Fifth Avenue, Kelby Park, SA, 5099 Australia</p>
  </section>

  <section class="card card--back" aria-label="Business card back">
    <div class="band band--panel"></div>
    <div class="band band--strip" role="img" aria-label="Decorative green colour band"></div>
    <p class="address">27 Fifth Avenue, Kelby Park, SA, 5099 Australia</p>
    <div class="brand">
      <span class="brand__mark"></span>
      <span>Harwell Bracegirdle<br>Consulting Pty Ltd</span>
    </div>
  </section>
</main>
</body>
</html>
```